Spring Style Exclusive Shopping Party for women

We need a postcard design for our Spring Shopping Event. Willow Lane is a women's apparel and accessories store featuring missy, petite and plus sizes. Event is Saturday, April 1 from 9am-10am. Looking for a twist on the spring shopping party idea. Attaching 2 postcards we have previously sent for this event and 2 ideas for what we are looking for in new postcard.

Target Market(s)

women 20+

Industry/Entity Type

Retail

Font styles to use
Serif

Requirements
Must have
• must be eye catching, have the logo, date and time of event,
Nice to have
• woman model

```html
<!DOCTYPE html>
<html lang="en">
<head>
<meta charset="utf-8">
<title>Spring Shopping Event – Willow Lane</title>
<link href="https://fonts.googleapis.com/css2?family=Great+Vibes&family=Marcellus&family=Marcellus+SC&family=Open+Sans:wght@300;700&display=swap" rel="stylesheet">
<style>
  :root {
    --blush: #fce6ee;
    --magenta: #d41c5c;
    --rose: #d81b60;
    --lime: #b6c33f;
    --ink: #141414;
    --white: #ffffff;
  }
  * { margin: 0; padding: 0; box-sizing: border-box; }
  html, body { width: 1200px; height: 929px; overflow: hidden; }
  body { background: var(--blush); }
  .postcard {
    position: relative;
    width: 1200px;
    height: 929px;
    background: var(--blush);
    overflow: hidden;
  }
  .frame-line { position: absolute; background: var(--magenta); }
  .frame-top { left: 575px; top: 29px; width: 605px; height: 4px; }
  .frame-right { left: 1176px; top: 29px; width: 4px; height: 878px; }
  .frame-bottom { left: 27px; top: 903px; width: 1153px; height: 4px; }
  .frame-left { left: 27px; top: 438px; width: 4px; height: 469px; }

  .floral-art {
    position: absolute;
    left: 0; top: 0;
    width: 560px; height: 420px;
    background:
      radial-gradient(ellipse 260px 200px at 120px 140px, #e9708f 0%, rgba(233,112,143,0.6) 50%, rgba(252,230,238,0) 100%),
      radial-gradient(ellipse 160px 110px at 420px 80px, rgba(205,30,110,0.75) 0%, rgba(252,230,238,0) 100%);
  }

  .title {
    position: absolute;
    left: 450px; top: 58px;
    width: 720px;
    text-align: center;
    font-family: "Great Vibes", cursive;
    color: var(--rose);
    font-size: 118px;
    line-height: 98px;
  }
  .rule { position: absolute; background: var(--magenta); height: 2px; }
  .rule-long { left: 452px; top: 298px; width: 716px; }
  .rule-short { left: 503px; top: 307px; width: 612px; height: 1px; }

  .brand-name {
    position: absolute;
    left: 450px; top: 338px;
    width: 720px;
    text-align: center;
    font-family: "Marcellus", serif;
    font-size: 54px;
    color: var(--ink);
    letter-spacing: 1px;
  }
  .store-tagline {
    position: absolute;
    left: 450px; top: 448px;
    width: 722px;
    text-align: center;
    font-family: "Marcellus SC", serif;
    font-size: 29px;
    color: var(--magenta);
    letter-spacing: 0.5px;
  }

  .date-band {
    position: absolute;
    left: 0; top: 493px;
    width: 1200px; height: 165px;
    background: var(--magenta);
  }
  .event-time {
    position: absolute;
    left: 455px; top: 512px;
    width: 720px;
    text-align: center;
    font-family: "Marcellus SC", serif;
    color: var(--white);
    line-height: 66px;
  }
  .event-time .day { display: block; font-size: 62px; letter-spacing: 2px; }
  .event-time .hours { display: block; font-size: 60px; letter-spacing: 2px; }

  .offer-burst { position: absolute; left: 50px; top: 387px; width: 380px; height: 380px; }
  .offer-text {
    position: absolute;
    left: 50px; top: 487px;
    width: 380px;
    text-align: center;
    font-family: "Open Sans", sans-serif;
    font-weight: 700;
    color: var(--rose);
    line-height: 56px;
  }
  .offer-text .amount { display: block; font-size: 56px; }
  .offer-text .scope { display: block; font-size: 52px; line-height: 50px; }

  .event-note {
    position: absolute;
    left: 480px; top: 712px;
    width: 660px;
    text-align: center;
    font-family: "Open Sans", sans-serif;
    font-weight: 300;
    font-size: 28px;
    line-height: 42px;
    color: var(--magenta);
  }
</style>
</head>
<body>
<main class="postcard">
  <div class="floral-art" role="img" aria-label="Illustration of pink dahlias, roses and buds on green stems"></div>

  <div class="frame-line frame-top"></div>
  <div class="frame-line frame-right"></div>
  <div class="frame-line frame-bottom"></div>
  <div class="frame-line frame-left"></div>

  <h1 class="title">Spring<br>Shopping Event</h1>
  <div class="rule rule-long"></div>
  <div class="rule rule-short"></div>

  <div class="brand-name">Willow Lane</div>
  <p class="store-tagline">Women’s apparel and accessories store</p>

  <div class="date-band"></div>
  <p class="event-time">
    <span class="day">Saturday, April 1</span>
    <span class="hours">from 9am-10am</span>
  </p>

  <svg class="offer-burst" viewBox="-190 -190 380 380" aria-hidden="true">
    <g fill="var(--lime)">
      <polygon points="190,0 95,164.5 -95,164.5 -190,0 -95,-164.5 95,-164.5"/>
      <polygon points="190,0 95,164.5 -95,164.5 -190,0 -95,-164.5 95,-164.5" transform="rotate(15)"/>
      <polygon points="190,0 95,164.5 -95,164.5 -190,0 -95,-164.5 95,-164.5" transform="rotate(30)"/>
      <polygon points="190,0 95,164.5 -95,164.5 -190,0 -95,-164.5 95,-164.5" transform="rotate(45)"/>
    </g>
  </svg>
  <p class="offer-text">
    <span class="amount">30% OFF</span>
    <span class="scope">entire</span>
    <span class="scope">purchase</span>
  </p>

  <p class="event-note">Our staff will be on hand to provide<br>an inside look at our favorite items for the<br>upcoming spring and summer season!</p>
</main>
</body>
</html>
```